Kitchen Tools Infographic - Helpful Items for Healthy Home Meals

We are a weight loss company that provides holistic, natural nutrition programs to consumers -- you can see our web site at www.FernaluVita.com. We need a simple infographic to be shared on social media and via email. The topic for the infographic is "Equip Your Kitchen for Healthy Home Meals". We've outlined 5 groups of kitchen tools that are helpful for consumers to have for preparing home meals, and included some framing statistics emphasizing the weight management benefits of preparing meals versus eating out.

Target Market(s)

Women age 35-55

Industry/Entity Type

Health And Wellness

Font styles to use
Sans Serif

Colors
0292cd
9bcb3b

Requirements
Must have
• - FernaluVita Logo
• - Graphics summarizing statistic (weight gain)
• - Graphics showing groupings of kitchen tools
Should not have
• body scale graphics
• before/after graphics

```html
<!DOCTYPE html>
<html lang="en">
<head>
<meta charset="utf-8">
<title>Equip Your Kitchen for Healthy Home Meals</title>
<link rel="stylesheet" href="https://fonts.googleapis.com/css2?family=Architects+Daughter&family=Roboto+Condensed:wght@500;700&family=Source+Sans+3:ital,wght@0,400;0,600;0,700;1,700&display=swap">
<style>
:root{
  --blue:#0292cd;
  --green:#9bcb3b;
  --orange:#f7941d;
  --charcoal:#3d3d3f;
  --panel:#ededed;
  --ink:#2b2b2b;
  --white:#ffffff;
}
*{margin:0;padding:0;box-sizing:border-box}
html,body{width:1200px;height:2250px;overflow:hidden}
body{position:relative;background:var(--charcoal);font-family:"Source Sans 3",Arial,sans-serif;color:var(--ink)}
.abs{position:absolute}

/* header */
.title-bar{left:105px;top:28px;width:990px;height:74px;background:var(--orange);display:flex;align-items:center;justify-content:center}
.title-bar h1{font-family:"Roboto Condensed",Arial Narrow,sans-serif;font-weight:500;font-size:56px;color:#222;letter-spacing:-0.5px;white-space:nowrap}
.why{left:0;top:108px;width:1200px;text-align:center;font-weight:700;font-size:44px;color:var(--green)}
.intro{left:22px;top:162px;width:1160px;font-size:27px;line-height:36px;color:var(--white)}
.intro strong{font-style:italic;font-weight:700}

/* charts */
.charts{left:0;top:285px;width:1200px;height:398px;background:var(--white)}
.charts text{font-family:"Source Sans 3",Arial,sans-serif}
.axis-num{font-size:21px;fill:var(--ink)}
.bar-label{font-size:17px;fill:var(--ink)}
.bar-label--blue{fill:var(--blue)}
.chart-caption{font-size:22px;fill:var(--ink)}

/* tools banner */
.tools-banner{left:0;top:683px;width:1200px;height:120px;background:var(--charcoal);font-family:"Architects Daughter",cursive;color:var(--white)}
.tools-banner p{position:absolute;left:60px;top:26px;font-size:39px;white-space:nowrap;display:flex;align-items:baseline}
.tools-banner span{font-size:56px;color:var(--green);margin-left:14px}

.tools-panel{left:0;top:803px;width:1200px;height:1207px;background:var(--panel)}
.route{left:0;top:790px}
.ring-num{font-family:"Source Sans 3",Arial,sans-serif;font-weight:700;font-size:112px;fill:var(--white)}

/* group tags */
.tag{height:68px;width:174px;display:flex;align-items:center;font-weight:700;font-size:40px;color:var(--white);letter-spacing:0.5px}
.tag--right{left:240px;background:var(--blue);clip-path:polygon(0 0,86% 0,100% 50%,86% 100%,0 100%);padding-left:22px}
.tag--left{left:783px;background:var(--green);clip-path:polygon(14% 0,100% 0,100% 100%,14% 100%,0 50%);padding-left:40px}
.tag--prep{top:891px}.tag--tech{top:1123px}.tag--cook{top:1355px}.tag--serve{top:1587px}.tag--store{top:1819px}

/* tool art placeholders */
.art{border-radius:8px}
.art--board{left:450px;top:878px;width:158px;height:67px;background:#c8905a}
.art--knife{left:693px;top:905px;width:170px;height:22px;background:#c9ccd0;border-radius:11px}
.art--scale{left:870px;top:858px;width:150px;height:90px;background:#f5b915}
.art--blender{left:60px;top:1058px;width:75px;height:130px;background:#8dc63f}
.art--slow{left:330px;top:1110px;width:128px;height:75px;background:#3d4a5c}
.art--pressure{left:585px;top:1110px;width:180px;height:78px;background:#f7c300}
.art--pan{left:450px;top:1305px;width:112px;height:115px;background:#2b2f3a;border-radius:50%}
.art--steamer{left:705px;top:1305px;width:83px;height:113px;background:#3aa3c8}
.art--sheet{left:975px;top:1352px;width:90px;height:66px;background:#5b1f2a}
.art--napkin{left:75px;top:1545px;width:90px;height:90px;background:#e0403a}
.art--dinner{left:277px;top:1537px;width:128px;height:98px;background:#d4d0c8}
.art--plates{left:577px;top:1545px;width:105px;height:100px;background:#dcd9d4;border-radius:50%}
.art--glass{left:495px;top:1775px;width:90px;height:108px;background:#dfeaf0}
.art--jar{left:750px;top:1783px;width:68px;height:100px;background:#f4a5b8}
.art--bag{left:990px;top:1775px;width:75px;height:108px;background:#e2e3e5}

/* tool text */
.tool{font-size:15px;line-height:18px}
.tool p{white-space:nowrap}
.tool h3{font-size:18px;font-weight:700;line-height:22px;color:var(--blue)}
.tool--dark h3{color:var(--ink)}
.tool--center{text-align:center;width:270px}
.tool--left{text-align:left}

.t-board{left:390px;top:962px}
.t-knife{left:645px;top:962px}
.t-scale{left:900px;top:962px}
.t-blender{left:45px;top:1200px;width:230px}
.t-slow{left:330px;top:1200px;width:230px}
.t-pressure{left:572px;top:1200px;width:210px}
.t-blender h3{text-align:left}
.t-slow h3,.t-pressure h3{text-align:center}
.t-pan{left:400px;top:1430px;width:240px}
.t-steamer{left:645px;top:1430px;width:220px}
.t-sheet{left:905px;top:1430px;width:280px}
.t-pan h3,.t-steamer h3,.t-sheet h3{text-align:center}
.t-napkin{left:35px;top:1660px;width:180px}
.t-dinner{left:240px;top:1660px;width:240px}
.t-plates{left:500px;top:1660px;width:270px}
.t-napkin h3,.t-dinner h3,.t-plates h3{text-align:center}
.t-glass{left:405px;top:1895px}
.t-jar{left:660px;top:1895px}
.t-bag{left:900px;top:1895px}

/* footer */
.footer{left:0;top:2010px;width:1200px;height:240px;background:var(--charcoal);border-top:5px solid #d7dcd0}
.footer-line{left:0;top:2030px;width:1200px;text-align:center;font-weight:700;font-size:28px;color:var(--white)}
.footer-invite{left:0;top:2070px;width:1200px;text-align:center;font-weight:700;font-size:28px;color:var(--green)}
.contact-btn{left:492px;top:2115px;width:220px;height:38px;background:var(--green);color:#222;font-weight:700;font-size:22px;display:flex;align-items:center;justify-content:center;letter-spacing:0.5px}
.brand{left:24px;top:2150px;font-size:64px;font-weight:400;color:var(--blue);letter-spacing:1px}
.site{right:22px;top:2184px;font-size:32px;font-weight:700;color:var(--white)}
</style>
</head>
<body>

<header>
  <div class="abs title-bar"><h1>Equip Your Kitchen for Healthy HomeMeals</h1></div>
  <h2 class="abs why">Why Cook at Home?</h2>
  <p class="abs intro">Those who eat out consume an average of 134 calories more per meal.<br><strong>Americans eat out an average of 4.5 times per week</strong>, so those extra calories can add up to substantial weight gain -- and give you a reason to prepare your own meals.</p>
</header>

<section class="abs charts">
  <svg width="1200" height="398" viewBox="0 0 1200 398">
    <g stroke="#333" stroke-width="1.5">
      <line x1="97" y1="18" x2="97" y2="312"/>
      <line x1="97" y1="312" x2="435" y2="312"/>
    </g>
    <g class="axis-num" text-anchor="end">
      <text x="88" y="34">700</text><text x="88" y="75">600</text><text x="88" y="116">500</text>
      <text x="88" y="156">400</text><text x="88" y="197">300</text><text x="88" y="238">200</text>
      <text x="88" y="278">100</text><text x="88" y="319">0</text>
    </g>
    <g stroke="#333" stroke-width="1.5" stroke-dasharray="6 5">
      <line x1="90" y1="67" x2="162" y2="67"/>
      <line x1="90" y1="257" x2="315" y2="257"/>
    </g>
    <rect x="162" y="67" width="27" height="245" fill="#0292cd"/>
    <rect x="315" y="257" width="27" height="55" fill="#9bcb3b"/>
    <text class="bar-label bar-label--blue" x="175" y="334" text-anchor="middle">Calories per week</text>
    <text class="bar-label" x="330" y="334" text-anchor="middle">Calories per meal</text>
    <text class="chart-caption" x="30" y="383">Excess Calories from Restaurant Meals</text>
    <line x1="0" y1="393" x2="465" y2="393" stroke="#333" stroke-width="1.5"/>

    <g stroke="#333" stroke-width="1.5">
      <line x1="810" y1="2" x2="810" y2="312"/>
      <line x1="810" y1="312" x2="1150" y2="312"/>
    </g>
    <g class="axis-num" text-anchor="end">
      <text x="796" y="115">10</text><text x="796" y="156">8</text><text x="796" y="197">6</text>
      <text x="796" y="238">4</text><text x="796" y="278">2</text><text x="796" y="319">0</text>
    </g>
    <g stroke="#333" stroke-width="1.5" stroke-dasharray="6 5">
      <line x1="810" y1="297" x2="840" y2="297"/>
      <line x1="810" y1="220" x2="952" y2="220"/>
      <line x1="810" y1="128" x2="1150" y2="128"/>
    </g>
    <rect x="840" y="297" width="27" height="15" fill="#0292cd"/>
    <rect x="952" y="220" width="28" height="92" fill="#9bcb3b"/>
    <rect x="1070" y="128" width="27" height="184" fill="#0292cd"/>
    <text class="bar-label bar-label--blue" x="853" y="334" text-anchor="middle">2 months</text>
    <text class="bar-label" x="966" y="334" text-anchor="middle">6 months</text>
    <text class="bar-label bar-label--blue" x="1083" y="334" text-anchor="middle">1 year</text>
    <text class="chart-caption" x="735" y="383">Pounds Gained from Restaurant Meals</text>
    <line x1="720" y1="393" x2="1170" y2="393" stroke="#333" stroke-width="1.5"/>
  </svg>
</section>

<div class="abs tools-banner"><p>Make healthy eating easier with these<span>Kitchen Tools:</span></p></div>
<div class="abs tools-panel"></div>

<svg class="abs route" width="1200" height="1230" viewBox="0 790 1200 1230">
  <path d="M660 790 V809 H135 A116 116 0 0 0 135 1041 H1058 A116 116 0 0 1 1058 1273 H135 A116 116 0 0 0 135 1505 H1058 A116 116 0 0 1 1058 1737 H135 A116 116 0 0 0 135 1969 H652 V2010" fill="none" stroke="#f7941d" stroke-width="14"/>
  <g>
    <circle cx="135" cy="925" r="104" fill="#3d3d3f"/><circle cx="135" cy="925" r="88" fill="#fff"/><circle cx="135" cy="925" r="77" fill="#0292cd"/>
    <text class="ring-num" x="135" y="964" text-anchor="middle">1</text>
    <circle cx="1058" cy="1157" r="104" fill="#3d3d3f"/><circle cx="1058" cy="1157" r="88" fill="#fff"/><circle cx="1058" cy="1157" r="77" fill="#9bcb3b"/>
    <text class="ring-num" x="1058" y="1196" text-anchor="middle">2</text>
    <circle cx="135" cy="1389" r="104" fill="#3d3d3f"/><circle cx="135" cy="1389" r="88" fill="#fff"/><circle cx="135" cy="1389" r="77" fill="#0292cd"/>
    <text class="ring-num" x="135" y="1428" text-anchor="middle">3</text>
    <circle cx="1058" cy="1621" r="104" fill="#3d3d3f"/><circle cx="1058" cy="1621" r="88" fill="#fff"/><circle cx="1058" cy="1621" r="77" fill="#9bcb3b"/>
    <text class="ring-num" x="1058" y="1660" text-anchor="middle">4</text>
    <circle cx="135" cy="1853" r="104" fill="#3d3d3f"/><circle cx="135" cy="1853" r="88" fill="#fff"/><circle cx="135" cy="1853" r="77" fill="#0292cd"/>
    <text class="ring-num" x="135" y="1892" text-anchor="middle">5</text>
  </g>
</svg>

<div class="abs tag tag--right tag--prep">PREP</div>
<div class="abs tag tag--left tag--tech">TECH</div>
<div class="abs tag tag--right tag--cook">COOK</div>
<div class="abs tag tag--left tag--serve">SERVE</div>
<div class="abs tag tag--right tag--store">STORE</div>

<!-- prep -->
<div class="abs art art--board" role="img" aria-label="Wooden cutting board illustration"></div>
<div class="abs art art--knife" role="img" aria-label="Chef's knife illustration"></div>
<div class="abs art art--scale" role="img" aria-label="Yellow digital food scale illustration"></div>
<div class="abs tool tool--center t-board"><h3>Cutting Board</h3><p>essential for prepping meat<br>and vegetables</p></div>
<div class="abs tool tool--center t-knife"><h3>Chef’s Knife</h3><p>go for quality to make chopping,<br>dicing and slicing faster and easier</p></div>
<div class="abs tool tool--center t-scale"><h3>Digital Food Scale</h3><p>get the precision you need for<br>perfect recipes and portion control</p></div>

<!-- tech -->
<div class="abs art art--blender" role="img" aria-label="High-powered blender illustration"></div>
<div class="abs art art--slow" role="img" aria-label="Slow cooker illustration"></div>
<div class="abs art art--pressure" role="img" aria-label="Yellow pressure cooker illustration"></div>
<div class="abs tool tool--left tool--dark t-blender"><h3>High-Powered Blender</h3><p>make highly nutritious, healthy<br>drinks from fruits and veggies</p></div>
<div class="abs tool tool--left tool--dark t-slow"><h3>Slow Cooker</h3><p>cook delicious meals while you<br>are at work</p></div>
<div class="abs tool tool--left tool--dark t-pressure"><h3>Pressure Cooker</h3><p>create single pot meals in<br>20 minutes or less</p></div>

<!-- cook -->
<div class="abs art art--pan" role="img" aria-label="Ceramic frying pan illustration"></div>
<div class="abs art art--steamer" role="img" aria-label="Vegetable steamer illustration"></div>
<div class="abs art art--sheet" role="img" aria-label="Baking sheet illustration"></div>
<div class="abs tool tool--left t-pan"><h3>Ceramic Pan</h3><p>nonstick cooking surface allows<br>you to cook without oil</p></div>
<div class="abs tool tool--left t-steamer"><h3>Vegetable Steamer</h3><p>preserve nutrients and natural,<br>fresh taste</p></div>
<div class="abs tool tool--left t-sheet"><h3>Baking Sheet</h3><p>ideal for roasting vegetables in the<br>oven or baking chicken and fish dishes</p></div>

<!-- serve -->
<div class="abs art art--napkin" role="img" aria-label="Red checked cloth napkin illustration"></div>
<div class="abs art art--dinner" role="img" aria-label="Plate with fork and spoon illustration"></div>
<div class="abs art art--plates" role="img" aria-label="Stacked small plates illustration"></div>
<div class="abs tool tool--left tool--dark t-napkin"><h3>Cloth Napkins</h3><p>to reduce waste and dress<br>up your table</p></div>
<div class="abs tool tool--left tool--dark t-dinner"><h3>Dinnerware</h3><p>pre-plate meals rather than serving<br>family style to control portions</p></div>
<div class="abs tool tool--left tool--dark t-plates"><h3>Small Plates</h3><p>use salad plates and smaller dishware to<br>manage perception of food volume</p></div>

<!-- store -->
<div class="abs art art--glass" role="img" aria-label="Glass storage containers illustration"></div>
<div class="abs art art--jar" role="img" aria-label="Pink mason jar illustration"></div>
<div class="abs art art--bag" role="img" aria-label="Re-sealable freezer bag illustration"></div>
<div class="abs tool tool--center t-glass"><h3>Glass Storage Containers</h3><p>keep your healthy leftovers so<br>nothing goes to waste</p></div>
<div class="abs tool tool--center t-jar"><h3>Mason Jars</h3><p>perfect for premade salads<br>that you can bring to work</p></div>
<div class="abs tool tool--center t-bag"><h3>Freezer Safe Re-Sealable Bags</h3><p>prepare double batches to make the<br>most of your time</p></div>

<footer>
  <div class="abs footer"></div>
  <p class="abs footer-line">FernaluVita can help you develop healthier eating habits.</p>
  <p class="abs footer-invite">We invite you to learn more.</p>
  <div class="abs contact-btn">CONTACT US</div>
  <div class="abs brand">FernaluVita</div>
  <div class="abs site">www.FernaluVita.com</div>
</footer>

</body>
</html>
```